Canned Beveraged Design - 473 mL Seltzer

We need to design a line extension of an existing product into a new beverage category. We currently market a Craft Soda, in an alcoholic and non-alcoholic version. We wish to market a Seltzer, sugar free, version of the same brand. Its a different product (from extremely sweet to 0 sugar and very light). So we need to communicate the attributes of this new product while making sure that consumers can still recognize and see the existing brand in the new product.

We have attached pictures of the existing product for your reference. The cans are the alcoolic version of the product and the bottles are the non-alcoolic version.
To develop the product, use a cherry seltzer flavor as a reference but the design should be able to be declined into other flavours and colours easily.

Target Market(s)

Consumers of the traditionnal product are consummers aged 45-65 who are nostalgic of the brand which was extremely strong 40 ago. These consumers remember going to the corner store and getting a fizz cabin as a treat. However, they are now more health conscious and looking to cut sugar and calories from their day to day diet and therefore looking for an alternative like an alcoholic seltzer rather than a alcohollic hard soda.

Requirements
Must have
• It must be a 473 mL. It must communicate the Fizz Cabin brand and name feel. It must communicate that the product is light in flavor, easy to drink and contains 0 sugar.

```html
<!DOCTYPE html>
<html lang="en">
<head>
<meta charset="utf-8">
<title>Fizz Cabin Hard Soda – Can Label</title>
<link rel="stylesheet" href="https://fonts.googleapis.com/css2?family=Poppins:wght@600;700&family=Roboto+Condensed:wght@400;700&display=swap">
<style>
  :root{
    --bg-light:#eef0f4;
    --bg-dark:#c9ccd4;
    --maroon:#7a1f3d;
    --maroon-deep:#4a0f22;
    --maroon-soft:#b98a9a;
    --ink:#111111;
    --label-white:#f6f6f6;
    --paper:#ffffff;
  }
  *{box-sizing:border-box;margin:0;padding:0}
  html,body{width:1200px;height:1038px;overflow:hidden}
  body{
    background:radial-gradient(ellipse at 50% 40%,var(--bg-light) 0%,var(--bg-dark) 100%);
    font-family:"Roboto Condensed",sans-serif;
    position:relative;
  }
  .panel{
    position:absolute;top:80px;width:326px;height:856px;
    background:var(--label-white);
    overflow:hidden;border-radius:6px;
  }
  .panel-front{left:230px}
  .panel-back{left:650px}

  .top-band{
    position:absolute;top:20px;left:0;right:0;height:40px;
    background:var(--maroon);color:var(--paper);
    font-family:"Roboto Condensed",sans-serif;font-size:20px;letter-spacing:.5px;
    display:flex;align-items:center;justify-content:center;
    white-space:nowrap;overflow:hidden;
  }

  .brand-name{
    position:absolute;top:95px;left:0;right:0;text-align:center;
    font-family:"Poppins",sans-serif;font-weight:700;color:var(--ink);
    line-height:.95;
  }
  .brand-name .word-main{display:block;font-size:112px;letter-spacing:-3px}
  .brand-name .word-sub{display:block;font-size:74px;letter-spacing:-2px}

  .ribbon{
    position:absolute;top:375px;left:6px;right:6px;height:36px;
    background:var(--maroon);color:var(--paper);
    clip-path:polygon(0 0,100% 0,96% 50%,100% 100%,0 100%,4% 50%);
    display:flex;align-items:center;justify-content:center;
    font-size:21px;
  }
  .ribbon .sep{margin:0 8px}

  .swirl-art{
    position:absolute;left:0;right:0;top:450px;bottom:0;
    background:linear-gradient(180deg,var(--maroon) 0%,var(--maroon-deep) 100%);
    clip-path:ellipse(95% 100% at 50% 100%);
  }

  .abv-label{
    position:absolute;top:720px;left:4px;width:300px;height:52px;
    background:var(--paper);border-radius:26px;
    display:flex;flex-direction:column;justify-content:center;padding-left:34px;
    color:var(--maroon-deep);font-family:"Poppins",sans-serif;
  }
  .abv-label .line-en{font-size:11px;font-weight:600;letter-spacing:.6px;padding-left:10px}
  .abv-label .line-fr{font-size:11px;font-weight:700;letter-spacing:.4px}
  .abv-badge{
    position:absolute;top:714px;left:264px;width:56px;height:56px;border-radius:50%;
    background:var(--paper);border:2px solid var(--maroon-deep);
    display:flex;flex-direction:column;align-items:center;justify-content:center;
    color:var(--ink);line-height:1;
  }
  .abv-badge .pct{font-size:26px;font-weight:700}
  .abv-badge .unit{font-size:8px}
  .volume{
    position:absolute;top:790px;left:0;right:0;text-align:center;
    color:var(--paper);font-family:"Poppins",sans-serif;font-size:22px;font-weight:600;
  }

  /* back */
  .back-fade{
    position:absolute;left:0;right:0;top:620px;bottom:0;
    background:linear-gradient(180deg,rgba(185,138,154,0) 0%,var(--maroon-soft) 60%,var(--maroon) 100%);
  }
  .side-art{
    position:absolute;right:0;top:640px;width:42px;height:200px;
    background:linear-gradient(180deg,var(--maroon-soft),var(--maroon));
    border-radius:42px 0 0 42px;
  }
  .nutrition{
    position:absolute;top:90px;left:50px;width:232px;
    background:var(--paper);border:1.5px solid var(--ink);padding:4px 4px 5px;
    color:var(--ink);font-size:12px;line-height:1.35;
  }
  .nutrition-head{display:flex;justify-content:space-between;align-items:flex-start}
  .nutrition-title{font-size:24px;font-weight:700;line-height:1}
  .nutrition-mark{font-family:"Poppins",sans-serif;font-weight:700;font-size:11px;line-height:1;text-align:right;padding-top:4px}
  .serving{font-size:11px;border-bottom:7px solid var(--ink);padding-bottom:3px}
  .row{display:flex;justify-content:space-between;border-bottom:1px solid var(--ink)}
  .row.bold{font-weight:700}
  .row.indent{padding-left:12px}
  .row.thick{border-bottom:6px solid var(--ink)}
  .row.dv{justify-content:flex-end;font-size:10px;font-weight:700;border-bottom:1px solid var(--ink)}
  .nutrition-note{font-size:9.5px;line-height:1.3;padding-top:2px}

  .back-copy{
    position:absolute;top:474px;left:42px;width:250px;color:var(--ink);
    font-size:14px;line-height:1.18;
  }
  .back-copy p{margin-bottom:12px}
  .back-copy strong{font-weight:700}
  .origin{margin-bottom:10px}
  .claims{display:flex;align-items:center;gap:8px}
  .claims svg{flex:none}
</style>
</head>
<body>

<section class="panel panel-front" aria-label="Front label">
  <div class="top-band">EXTREMELY SWEET TO 0 SUGAR AND VERY LIGHT</div>

  <h1 class="brand-name">
    <span class="word-main">Fizz</span>
    <span class="word-sub">Cabin</span>
  </h1>

  <div class="ribbon"><span>Hard soda</span><span class="sep">|</span><span>CREAM SODA</span></div>

  <div class="swirl-art" role="img" aria-label="Decorative pattern of layered maroon concentric circles"></div>

  <div class="abv-label">
    <span class="line-en">ALCOHOLIC VODKA BEVERAGE</span>
    <span class="line-fr">BOISSON ALCOOLISEE A LA VODKA</span>
  </div>
  <div class="abv-badge"><span class="pct">7%</span><span class="unit">alc./vol.</span></div>
  <div class="volume">473mL</div>
</section>

<section class="panel panel-back" aria-label="Back label">
  <div class="back-fade"></div>
  <div class="side-art" role="img" aria-label="Decorative maroon concentric circles at the edge"></div>
  <div class="top-band">EXTREMELY SWEET TO 0 SUGAR AND VERY LIGHT</div>

  <div class="nutrition">
    <div class="nutrition-head">
      <div class="nutrition-title">Nutrition Facts</div>
      <div class="nutrition-mark">Fizz<br>Cabin</div>
    </div>
    <div class="serving">Serving Size 1oz (28g)</div>
    <div class="row bold" style="border-bottom:1px solid var(--ink)"><span>Amount Per Serving</span></div>
    <div class="row thick"><span>Calories 110</span><span>Calories from Fat 60</span></div>
    <div class="row dv"><span>% Daily Value*</span></div>
    <div class="row"><span>Total Fat 7g</span><span>11%</span></div>
    <div class="row indent"><span>Saturated Fat 4g</span><span>21%</span></div>
    <div class="row indent"><span>Trans Fat 0g</span><span></span></div>
    <div class="row"><span>Cholesterol 0mg</span><span>0%</span></div>
    <div class="row"><span>Sodium 0mg</span><span>0%</span></div>
    <div class="row"><span>Total Carbohydrate 14g</span><span>5%</span></div>
    <div class="row indent"><span>Dietary Fiber 2g</span><span>8%</span></div>
    <div class="row indent"><span>Sugars 10g</span><span></span></div>
    <div class="row thick"><span>Protein 1g</span><span>2%</span></div>
    <div class="row"><span>Vitamin A 0%</span><span>• &nbsp;Vitamin C 1%</span></div>
    <div class="row"><span>Calcium 1%</span><span>• &nbsp;Iron 4%</span></div>
    <p class="nutrition-note">*Percent Daily Values are based on a 2,000 calorie diet. Your daily values may be higher or lower depending on your calorie needs:</p>
  </div>

  <div class="back-copy">
    <p><strong>INGREDIENTS:</strong> Organic dark chocolate (organic dried cane syrup, organic chocolate liquor, organic cocoa butter, organic soy lecithin, and organic vanilla), organic pomegranate arils, organic gum arabic, and organic confectioners glaze.</p>
    <p><strong>Allergy Information:</strong> Manufactured on shared equipment with milk-containing products and tree nuts. Milk or nuts may be present.</p>
    <p>Keep at room temperature (65° - 75°F).</p>
    <p class="origin">Product of India.<br>Processed and Packaged in USA.</p>
    <div class="claims">
      <span>Organic, Kosher, Non GMO.</span>
      <svg width="20" height="18" viewBox="0 0 20 18" aria-label="Recycle">
        <path d="M10 2 L14 9 M14 9 L6 9 M6 9 L10 2" fill="none" stroke="var(--ink)" stroke-width="2"/>
        <circle cx="10" cy="9" r="7.5" fill="none" stroke="var(--ink)" stroke-width="1.5"/>
      </svg>
      <svg width="18" height="22" viewBox="0 0 18 22" aria-label="Dispose properly">
        <circle cx="4" cy="4" r="2.5" fill="var(--ink)"/>
        <path d="M4 7 L4 14 L1 20 M4 10 L9 8" fill="none" stroke="var(--ink)" stroke-width="2"/>
        <rect x="10" y="9" width="7" height="11" fill="none" stroke="var(--ink)" stroke-width="1.5"/>
      </svg>
    </div>
  </div>
</section>

</body>
</html>
```